Business Card Design

I need a business card and logo for a new company based in Manhattan, Kansas called "Ferncliff Works, LLC". I am a project management consultant. I specialize in laying the foundation for businesses and business owners to get their projects on track. Think of it as if you were wanting to go from coast to coast on a train. Before you can jump on the train and sell tickets, you have to design the path the train will take, acquire the land, clear the trees, level the ground, prepare the base for the track, lay the track and finally place the train on the track (That's what I do with my clients). Once the train is on the track and I've provided them with the operations manual, then they and their managers get to drive the train. I don't have color preferences. The final design should communicate a clear direction or path to growing the customer's business.
Updates

Since I am in need of a logo as well, I have also created a logo design project that will work in conjunction with this project.

Reason: Accepted a company logo this afternoon that I would like to have cards designed around. Sorry for jumping the gun and posting both projects at the same time.

Industry/Entity Type

Business

Contact Information for Business Card

Owner: Dale Purvis. Business Name: Ferncliff Works, LLC. Business Address: 4871 Marlow Bend, Ridgeview, NE, 66921. Business Phone Number: 402-640-1572. Business Email: dale@ferncliffworksllc.example

```html
<!DOCTYPE html>
<html lang="en">
<head>
<meta charset="utf-8">
<title>Ferncliff Works, LLC — Business Card</title>
<link href="https://fonts.googleapis.com/css2?family=Lato:wght@400;700;900&display=swap" rel="stylesheet">
<style>
  :root {
    --backdrop: #2a2624;
    --card: #3a3a3c;
    --brand-blue: #1f5aa0;
    --accent-blue: #2a8ad8;
    --white: #ffffff;
    --soft-white: #e6e6e6;
  }
  * { margin: 0; padding: 0; box-sizing: border-box; }
  html, body {
    width: 1200px; height: 464px; overflow: hidden;
    background: var(--backdrop);
    font-family: "Lato", Arial, sans-serif;
  }
  .canvas { position: relative; width: 1200px; height: 464px; }
  .card {
    position: absolute; top: 78px;
    width: 540px; height: 309px;
    background: var(--card);
    overflow: hidden;
  }
  .card--back { left: 40px; }
  .card--front { left: 620px; }

  .back-wordmark {
    position: absolute; inset: 0;
    display: flex; align-items: center; justify-content: center; gap: 14px;
  }
  .brand-square { width: 30px; height: 30px; background: var(--brand-blue); flex: none; }
  .brand-name {
    color: var(--white); font-weight: 900; text-transform: uppercase;
    letter-spacing: 0.5px; line-height: 1.05;
  }
  .back-wordmark .brand-name { font-size: 34px; }

  .front-wordmark {
    position: absolute; left: 28px; top: 58px; width: 240px;
    display: flex; align-items: center; gap: 12px;
  }
  .front-wordmark .brand-square { width: 22px; height: 22px; }
  .front-wordmark .brand-name { font-size: 22px; }

  .divider {
    position: absolute; left: 285px; top: 34px;
    width: 2px; height: 132px; background: var(--accent-blue);
  }
  .contact {
    position: absolute; left: 312px; top: 42px; width: 222px;
    color: var(--soft-white);
  }
  .contact-name {
    color: var(--accent-blue); font-weight: 900; font-size: 17px;
    text-transform: uppercase; letter-spacing: 0.3px;
  }
  .contact-role {
    color: var(--white); font-size: 11px; text-transform: uppercase;
    letter-spacing: 0.6px; margin-top: 1px;
  }
  .contact-address {
    font-size: 9.5px; text-transform: uppercase; line-height: 1.45;
    margin-top: 20px; letter-spacing: 0.3px;
  }
  .contact-lines { margin-top: 16px; font-size: 9.5px; line-height: 2; white-space: nowrap; }
  .contact-label { color: var(--accent-blue); display: inline-block; width: 38px; }

  .band-stripe { position: absolute; left: 0; width: 100%; }
  .band-stripe--top-blue { top: 194px; height: 10px; background: var(--brand-blue); }
  .band-stripe--top-white { top: 207px; height: 3px; background: var(--white); }
  .band-web {
    position: absolute; left: 0; top: 213px; width: 100%; height: 48px;
    background: var(--brand-blue);
    display: flex; align-items: center; padding-left: 120px;
    color: var(--white); font-size: 15px; font-weight: 700; letter-spacing: 0.6px;
  }
  .band-stripe--bottom-white { top: 264px; height: 3px; background: var(--white); }
  .band-stripe--bottom-blue { top: 270px; bottom: 0; background: var(--brand-blue); }
</style>
</head>
<body>
<main class="canvas">
  <section class="card card--back" aria-label="Card back">
    <div class="back-wordmark">
      <span class="brand-square"></span>
      <span class="brand-name">Ferncliff Works,<br>LLC</span>
    </div>
  </section>

  <section class="card card--front" aria-label="Card front">
    <div class="front-wordmark">
      <span class="brand-square"></span>
      <span class="brand-name">Ferncliff Works,<br>LLC</span>
    </div>
    <div class="divider"></div>
    <div class="contact">
      <p class="contact-name">Dale Purvis</p>
      <p class="contact-role">Owner</p>
      <p class="contact-address">4871 Marlow Bend,<br>Ridgeview, NE, 66921</p>
      <p class="contact-lines">
        <span class="contact-label">Phone</span>: 402-640-1572<br>
        <span class="contact-label">Email</span>: dale@ferncliffworksllc.example
      </p>
    </div>
    <div class="band-stripe band-stripe--top-blue"></div>
    <div class="band-stripe band-stripe--top-white"></div>
    <div class="band-web">WWW.FERNCLIFFWORKS.EXAMPLE</div>
    <div class="band-stripe band-stripe--bottom-white"></div>
    <div class="band-stripe band-stripe--bottom-blue"></div>
  </section>
</main>
</body>
</html>
```